I need a business card for ALVA Holdings. We are a young startup based in New Zealand working in internet marketing and web development. The design should have some element connected to New Zealand, such as wave, koru or silver fern, just don't use a kiwi bird.

```html
<!DOCTYPE html>
<html lang="en">
<head>
<meta charset="utf-8">
<title>ALVA Holdings – Business Card</title>
<link rel="stylesheet" href="https://fonts.googleapis.com/css2?family=Open+Sans:wght@400;600;700&display=swap">
<style>
  :root {
    --stage: #1c1c1e;
    --card: #232324;
    --silver: #9a9a9c;
    --blue: #1479c4;
    --orange: #f0622a;
    --text: #e6e6e6;
    --muted: #bdbdbd;
    --rule: #3a3a3c;
  }
  * { margin: 0; padding: 0; box-sizing: border-box; }
  html, body { width: 1200px; height: 900px; overflow: hidden; }
  body {
    background: var(--stage);
    font-family: "Open Sans", Arial, sans-serif;
    position: relative;
  }
  .card {
    position: absolute;
    width: 560px;
    height: 320px;
    background: var(--card);
    border-radius: 18px;
    overflow: hidden;
  }
  .card-back { left: 60px; top: 90px; display: flex; align-items: center; justify-content: center; }
  .card-front { left: 580px; top: 490px; }

  .brand { display: flex; align-items: center; gap: 14px; position: relative; z-index: 1; }
  .brand-dot { width: 34px; height: 34px; border-radius: 50%; flex: none; }
  .brand-name { font-weight: 700; font-size: 40px; letter-spacing: 1px; line-height: 1; white-space: nowrap; }
  .card-back .brand-dot { background: var(--silver); }
  .card-back .brand-name { color: var(--silver); }

  .card-front .brand { position: absolute; right: 36px; top: 48px; }
  .card-front .brand-dot { background: var(--blue); width: 28px; height: 28px; }
  .card-front .brand-name { color: var(--blue); font-size: 34px; }

  /* Pacific wave line – the New Zealand element */
  .wave-rule {
    position: absolute; left: 0; top: 124px;
    width: 560px; height: 40px;
  }
  .wave-rule path { fill: none; stroke-linecap: round; }
  .wave-rule .wave-main { stroke: var(--blue); stroke-width: 2; }
  .wave-rule .wave-echo { stroke: var(--orange); stroke-width: 1.5; opacity: 0.8; }

  .card-back .wave-rule { top: auto; bottom: 34px; }
  .card-back .wave-rule .wave-main { stroke: var(--silver); opacity: 0.5; }
  .card-back .wave-rule .wave-echo { stroke: var(--silver); opacity: 0.3; }

  .person { position: absolute; left: 36px; top: 176px; }
  .person-name { color: var(--blue); font-weight: 700; font-size: 21px; letter-spacing: 0.5px; line-height: 1.1; }
  .person-role { color: var(--orange); font-size: 16px; line-height: 1.3; }

  .contacts { position: absolute; left: 36px; top: 236px; list-style: none; }
  .contacts li { display: flex; align-items: center; gap: 8px; color: var(--muted); font-size: 16px; line-height: 24px; }
  .contacts svg { width: 14px; height: 14px; fill: var(--blue); flex: none; }

  .address {
    position: absolute; right: 36px; top: 182px;
    text-align: right; color: var(--text); font-size: 15px; line-height: 1.35;
  }
</style>
</head>
<body>
  <section class="card card-back">
    <div class="brand">
      <span class="brand-dot"></span>
      <span class="brand-name">ALVA Holdings</span>
    </div>
    <svg class="wave-rule" viewBox="0 0 560 40" aria-hidden="true">
      <path class="wave-main" d="M36 20 C96 4 156 4 216 20 S336 36 396 20 S486 6 524 14"/>
      <path class="wave-echo" d="M36 28 C96 12 156 12 216 28 S336 44 396 28 S486 14 524 22"/>
    </svg>
  </section>

  <section class="card card-front">
    <div class="brand">
      <span class="brand-dot"></span>
      <span class="brand-name">ALVA Holdings</span>
    </div>

    <svg class="wave-rule" viewBox="0 0 560 40" aria-hidden="true">
      <path class="wave-main" d="M36 20 C96 4 156 4 216 20 S336 36 396 20 S486 6 524 14"/>
      <path class="wave-echo" d="M36 28 C96 12 156 12 216 28 S336 44 396 28 S486 14 524 22"/>
    </svg>

    <div class="person">
      <p class="person-name">MARCUS REID</p>
      <p class="person-role">Managing Director</p>
    </div>

    <ul class="contacts">
      <li>
        <svg viewBox="0 0 16 16" aria-hidden="true"><path d="M3 1h3l1.5 4-2 1.3a9 9 0 0 0 4.2 4.2L11 8.5l4 1.5v3a2 2 0 0 1-2 2A13 13 0 0 1 1 3a2 2 0 0 1 2-2z"/></svg>
        021-555 0147
      </li>
      <li>
        <svg viewBox="0 0 16 16" aria-hidden="true"><path d="M5 0h6a1.5 1.5 0 0 1 1.5 1.5v13A1.5 1.5 0 0 1 11 16H5a1.5 1.5 0 0 1-1.5-1.5v-13A1.5 1.5 0 0 1 5 0zm0 2v10.5h6V2zm3 11.3a.9.9 0 1 0 0 1.8.9.9 0 0 0 0-1.8z"/></svg>
        021-555 0147
      </li>
      <li>
        <svg viewBox="0 0 16 16" aria-hidden="true"><path d="M0 3h16v1.2L8 9 0 4.2zm0 2.6 8 4.8 8-4.8V13H0z"/></svg>
        hello@alvaholdings.nz
      </li>
    </ul>

    <p class="address">12345, Address Goes Here<br>Country Name, 123456</p>
  </section>
</body>
</html>
```